Flyer design needed for services offered and to show reviews from previous customers

I would like a Flyer designed showing some of the services i offer:
-LED lighting upgrades (pot lights, accent & commercial)
-Electrical repairs & Service work
- Fayglowen lighting
- TV wall mounts
My website is Voltarisa.ca if you need any photos from there in higher quality please let me know and i can provide them.

I want it to have a couple reviews from previous customers (attached links to facebook and google page)
Google:
https://revpage.example/r/QZ8kd4mtpWhaJXo/review
Facebook:
https://www.socialbook.example/Voltarisa-Contracting-Ltd-552918730461283

```html
<!DOCTYPE html>
<html lang="en">
<head>
<meta charset="UTF-8">
<title>Voltarisa Contracting – Flyer</title>
<link href="https://fonts.googleapis.com/css2?family=Outfit:wght@300;400;700&family=Nunito:wght@400;900&display=swap" rel="stylesheet">
<style>
  :root{
    --ink:#262a35;
    --panel:#30343f;
    --navy:#1d1e31;
    --red:#e3202a;
    --blue:#3a7cc4;
    --white:#ffffff;
    --muted:#d9dae3;
  }
  *{margin:0;padding:0;box-sizing:border-box}
  html,body{width:927px;height:1200px;overflow:hidden;background:var(--ink)}
  .flyer{position:relative;width:927px;height:1200px;overflow:hidden;background:var(--ink);font-family:"Outfit",sans-serif;color:var(--white)}
  .hero-art{position:absolute;inset:0}
  .headline{position:absolute;left:0;width:927px;top:566px;text-align:center;font-family:"Outfit",sans-serif;font-weight:700;font-size:49px;line-height:57px;letter-spacing:-0.5px}
  .headline .accent{color:var(--red)}
  .gallery{position:absolute;left:48px;top:793px;display:grid;grid-template-columns:162px 162px;column-gap:20px;row-gap:21px}
  .gallery .shot{height:101px;border:2px solid var(--red);border-radius:4px}
  .shot.living{background:linear-gradient(135deg,#c9cdd3,#8d9096 60%,#5e5f63)}
  .shot.tv-wall{background:linear-gradient(135deg,#e6e8ea,#b9bcc0 50%,#3b3d42)}
  .shot.house-night{background:linear-gradient(180deg,#2a2f5c,#7a2fd0 55%,#3b1d6a)}
  .shot.panel-box{background:linear-gradient(135deg,#d8d4cc,#5b5750 50%,#2a2826)}
  .about{position:absolute;left:463px;top:788px;width:410px}
  .about h2{font-family:"Nunito",sans-serif;font-weight:900;font-size:26px;line-height:32px;margin-bottom:10px}
  .about p{font-family:"Outfit",sans-serif;font-weight:300;font-size:11.2px;line-height:15.9px;color:var(--muted)}
  .services{position:absolute;left:463px;top:950px;list-style:none}
  .services li{position:relative;padding-left:36px;font-family:"Nunito",sans-serif;font-weight:900;font-size:22px;line-height:28px}
  .services li svg{position:absolute;left:0;top:6px}
  .services .detail{display:block;font-family:"Outfit",sans-serif;font-weight:300;font-size:19px;line-height:26px;margin-top:2px}
  .services li.s1{margin-bottom:14px}
  .services li.s2,.services li.s3{margin-bottom:12px}
  .contact{position:absolute;left:0;top:1036px;width:453px;height:164px;background:var(--panel);border-top-right-radius:38px}
  .brand{position:absolute;left:49px;top:21px;width:120px;height:120px;border:2px solid var(--white);border-radius:50%;display:flex;align-items:center;justify-content:center;font-family:"Outfit",sans-serif;font-weight:700;font-size:17px;letter-spacing:1px}
  .reach{position:absolute;left:191px;top:20px}
  .reach .lead{font-weight:300;font-size:16px;line-height:20px;margin-bottom:6px}
  .reach ul{list-style:none}
  .reach li{display:flex;align-items:center;height:29px;font-family:"Nunito",sans-serif;font-weight:900;font-size:19px}
  .reach .ico{width:18px;height:18px;background:var(--red);border-radius:3px;margin:0 12px 0 2px;display:flex;align-items:center;justify-content:center}
  .social{position:absolute;left:822px;top:1150px;display:flex;gap:5px}
  .social span{width:16px;height:16px;border-radius:50%;background:var(--red)}
</style>
</head>
<body>
<div class="flyer">
  <svg class="hero-art" width="927" height="1200" viewBox="0 0 927 1200">
    <defs>
      <linearGradient id="houseTones" x1="0" y1="0" x2="1" y2="0.3">
        <stop offset="0" stop-color="#c2249a"/>
        <stop offset="0.3" stop-color="#d86a3a"/>
        <stop offset="0.55" stop-color="#b8b43a"/>
        <stop offset="0.8" stop-color="#2ab7b0"/>
        <stop offset="1" stop-color="#3a5e9a"/>
      </linearGradient>
      <linearGradient id="skyFade" x1="0" y1="0" x2="0" y2="1">
        <stop offset="0" stop-color="#2f5b99"/>
        <stop offset="0.22" stop-color="#2f5b99" stop-opacity="0.6"/>
        <stop offset="0.5" stop-color="#2f5b99" stop-opacity="0"/>
      </linearGradient>
      <linearGradient id="lowerShade" x1="0" y1="0" x2="0" y2="1">
        <stop offset="0" stop-color="#26244a" stop-opacity="0.9"/>
        <stop offset="0.5" stop-color="#2a1f52" stop-opacity="0.95"/>
        <stop offset="1" stop-color="#1d1e31"/>
      </linearGradient>
    </defs>
    <g role="img" aria-label="Photo of a two-storey brick house at dusk outlined with rainbow permanent LED roof lights">
      <polygon points="319,0 600,0 927,224 927,1200 0,1200 0,224" fill="url(#houseTones)"/>
      <polygon points="319,0 600,0 927,224 927,1200 0,1200 0,224" fill="url(#skyFade)"/>
    </g>
    <polygon points="463,436 927,755 927,1200 0,1200 0,755" fill="url(#lowerShade)"/>
    <polygon points="463,470 927,790 927,1200 0,1200 0,790" fill="#1d1e31" opacity="0.45"/>
    <polygon points="313,0 319,0 0,224 0,220" fill="var(--white)"/>
    <polygon points="319,0 332,0 0,232 0,224" fill="var(--blue)"/>
    <polygon points="600,0 606,0 927,220 927,224" fill="var(--white)"/>
    <polygon points="588,0 600,0 927,224 927,232" fill="var(--blue)"/>
    <polygon points="463,395 927,716 927,755 463,436 0,755 0,716" fill="var(--white)"/>
  </svg>

  <h1 class="headline">LIGHTS TO<br><span class="accent">ILLUMINATE</span><br>HOMES AND HEARTS</h1>

  <div class="gallery">
    <div class="shot living" role="img" aria-label="Living room with new pot lights and mounted TV"></div>
    <div class="shot tv-wall" role="img" aria-label="TV mounted on a shiplap feature wall"></div>
    <div class="shot house-night" role="img" aria-label="House lit with purple exterior LED lights"></div>
    <div class="shot panel-box" role="img" aria-label="Open electrical breaker panel during service work"></div>
  </div>

  <section class="about">
    <h2>About Us</h2>
    <p>At Voltarisa contracting, we put a lot of thought into every little thing we do, making sure you’re getting high-quality and outstanding service. We aspire to provide you with the best professionals to ensure long-lasting results and transparently share our process every step of the way. Browse our website for additional information about our services and see how we can be of assistance.</p>
  </section>

  <ul class="services">
    <li class="s1"><svg width="20" height="20" viewBox="0 0 20 20"><circle cx="10" cy="10" r="10" fill="var(--red)"/><path d="M5 10h9M10.5 6l4 4-4 4" stroke="var(--white)" stroke-width="2.2" fill="none" stroke-linecap="round" stroke-linejoin="round"/></svg>LED lighting upgrades<span class="detail">(pot lights, accent &amp; commercial)</span></li>
    <li class="s2"><svg width="20" height="20" viewBox="0 0 20 20"><circle cx="10" cy="10" r="10" fill="var(--red)"/><path d="M5 10h9M10.5 6l4 4-4 4" stroke="var(--white)" stroke-width="2.2" fill="none" stroke-linecap="round" stroke-linejoin="round"/></svg>Electrical repairs &amp; Service work</li>
    <li class="s3"><svg width="20" height="20" viewBox="0 0 20 20"><circle cx="10" cy="10" r="10" fill="var(--red)"/><path d="M5 10h9M10.5 6l4 4-4 4" stroke="var(--white)" stroke-width="2.2" fill="none" stroke-linecap="round" stroke-linejoin="round"/></svg>Fayglowen lighting</li>
    <li><svg width="20" height="20" viewBox="0 0 20 20"><circle cx="10" cy="10" r="10" fill="var(--red)"/><path d="M5 10h9M10.5 6l4 4-4 4" stroke="var(--white)" stroke-width="2.2" fill="none" stroke-linecap="round" stroke-linejoin="round"/></svg>TV wall mounts</li>
  </ul>

  <footer class="contact">
    <div class="brand">VOLTARISA</div>
    <div class="reach">
      <p class="lead">For urgent matters call or text:</p>
      <ul>
        <li><span class="ico"><svg width="12" height="12" viewBox="0 0 24 24"><path d="M6.6 10.8a15 15 0 0 0 6.6 6.6l2.2-2.2a1 1 0 0 1 1-.25 11.4 11.4 0 0 0 3.6.57 1 1 0 0 1 1 1V20a1 1 0 0 1-1 1A17 17 0 0 1 3 4a1 1 0 0 1 1-1h3.5a1 1 0 0 1 1 1c0 1.25.2 2.45.57 3.57a1 1 0 0 1-.25 1z" fill="var(--white)"/></svg></span>(587) 555-0182</li>
        <li><span class="ico"><svg width="12" height="12" viewBox="0 0 24 24"><path d="M2 11 22 3l-6 18-4-7z" fill="var(--white)"/></svg></span>Dana@Voltarisa.ca</li>
        <li><span class="ico"><svg width="12" height="12" viewBox="0 0 24 24"><circle cx="12" cy="12" r="9" fill="none" stroke="var(--white)" stroke-width="2"/><path d="M3 12h18M12 3c3 3 3 15 0 18M12 3c-3 3-3 15 0 18" fill="none" stroke="var(--white)" stroke-width="1.6"/></svg></span>www.voltarisa.ca</li>
      </ul>
    </div>
  </footer>

  <div class="social"><span></span><span></span><span></span></div>
</div>
</body>
</html>
```